One name card with 4 companies logos

Hi, I would like to have a design of name card with my 4 companies logos incorporated into a single, 2-sided name card.

Information for name card:
1. Slogan "Transforming Lives"
2. Critical info: "Name", "Role", "Mobile Number", "Email", "Website"
3. Please follow the sequence in placing the logos (DVX, KRPE, Brivoquest, Nevo Foundation)

Page 1 of namecard - 4 Company Logos
Page 2 of namecard - Transforming Lives + Namecard information

B2B - Companies and government bodies

4. Please put this in the page 2 of card:
Accredited Training Provider
(7 logos/icons of different brands)

Designer to choose colors to be used in the design.

• Use white as a base color for namecard

```html
<!DOCTYPE html>
<html lang="en">
<head>
<meta charset="utf-8">
<title>Business Card – Details and Companies</title>
<link href="https://fonts.googleapis.com/css2?family=Lato:wght@400;700&display=swap" rel="stylesheet">
<style>
  :root {
    --page-bg: #e3e6ea;
    --card-white: #ffffff;
    --band: #eef1f5;
    --navy: #2b3d54;
    --blue: #4b6a98;
    --badge: #c9d3e0;
    --text-navy: #2b3d54;
    --text-muted: #7d8a9b;
    --text-white: #ffffff;
  }
  * { box-sizing: border-box; margin: 0; padding: 0; }
  html, body {
    width: 1200px;
    height: 1200px;
    overflow: hidden;
    background: var(--page-bg);
    font-family: "Lato", sans-serif;
  }
  .card {
    position: absolute;
    left: 170px;
    width: 860px;
    height: 480px;
    background: var(--card-white);
    overflow: hidden;
    box-shadow: 0 10px 24px rgba(0, 0, 0, 0.18);
  }
  .card--details { top: 50px; }
  .card--companies { top: 650px; }

  .card-art {
    position: absolute;
    inset: 0;
    width: 100%;
    height: 100%;
  }
  .logo-name {
    font-family: "Lato", sans-serif;
    font-weight: 700;
    text-anchor: middle;
    fill: var(--text-white);
  }

  .holder {
    position: absolute;
    left: 157px;
    top: 30px;
    color: var(--text-navy);
  }
  .holder-name {
    font-size: 30px;
    font-weight: 400;
    letter-spacing: 0.5px;
    line-height: 1.1;
  }
  .holder-role {
    font-size: 22px;
    color: var(--text-muted);
    margin-top: 2px;
  }
  .slogan {
    position: absolute;
    right: 40px;
    top: 40px;
    font-size: 17px;
    font-weight: 700;
    letter-spacing: 2px;
    color: var(--blue);
    text-transform: uppercase;
  }

  .contact-list {
    position: absolute;
    left: 322px;
    top: 0;
    list-style: none;
    color: var(--text-navy);
    font-size: 21px;
    letter-spacing: 0.4px;
  }
  .contact-item {
    position: absolute;
    white-space: nowrap;
    transform: translateY(-50%);
  }
  .contact-item--phone { top: 160px; word-spacing: 10px; }
  .contact-item--email { top: 228px; }
  .contact-item--web { top: 296px; }

  .accreditation-label {
    position: absolute;
    left: 157px;
    top: 350px;
    font-size: 15px;
    font-weight: 700;
    letter-spacing: 1.5px;
    text-transform: uppercase;
    color: var(--text-muted);
  }
</style>
</head>
<body>

<!-- Details side -->
<section class="card card--details">
  <svg class="card-art" viewBox="0 0 860 480" aria-hidden="true">
    <defs>
      <polygon id="hex" points="0,-46 42,-23 42,23 0,46 -42,23 -42,-23"/>
      <polygon id="hex-small" points="0,-26 23,-13 23,13 0,26 -23,13 -23,-13"/>
      <polygon id="hex-badge" points="0,-28 24,-14 24,14 0,28 -24,14 -24,-14"/>
    </defs>

    <!-- contact row bands -->
    <rect x="114" y="140" width="746" height="40" fill="var(--band)"/>
    <rect x="114" y="208" width="746" height="40" fill="var(--band)"/>
    <rect x="114" y="276" width="746" height="40" fill="var(--band)"/>

    <!-- company column -->
    <use href="#hex" x="57" y="4" fill="var(--blue)"/>
    <use href="#hex" x="57" y="100" fill="var(--navy)"/>
    <use href="#hex" x="57" y="195" fill="var(--blue)"/>
    <use href="#hex" x="57" y="290" fill="var(--navy)"/>
    <use href="#hex" x="57" y="385" fill="var(--blue)"/>
    <use href="#hex" x="57" y="482" fill="var(--navy)"/>

    <text class="logo-name" x="57" y="108" font-size="22">DVX</text>
    <text class="logo-name" x="57" y="202" font-size="18">KRPE</text>
    <text class="logo-name" x="57" y="295" font-size="12">Brivoquest</text>
    <text class="logo-name" x="57" y="382" font-size="13">Nevo</text>
    <text class="logo-name" x="57" y="397" font-size="11">Foundation</text>

    <!-- contact icons -->
    <use href="#hex-small" x="182" y="160" fill="var(--navy)"/>
    <use href="#hex-small" x="182" y="228" fill="var(--navy)"/>
    <use href="#hex-small" x="182" y="296" fill="var(--navy)"/>

    <g class="icon icon--phone" transform="translate(182 160)">
      <circle r="10" fill="var(--card-white)"/>
      <path d="M-4.5 -5 l2.5 -0.5 l1.5 3 l-1.5 1.2 a7 7 0 0 0 3.3 3.3 l1.2 -1.5 l3 1.5 l-0.5 2.5 a9 9 0 0 1 -9.5 -9.5 z" fill="var(--navy)"/>
    </g>
    <g class="icon icon--send" transform="translate(182 228)">
      <circle r="10" fill="var(--card-white)"/>
      <path d="M-5 0.5 L5 -5 L1 5 L-0.5 1.5 Z" fill="var(--navy)"/>
    </g>
    <g class="icon icon--home" transform="translate(182 296)">
      <circle r="10" fill="var(--card-white)"/>
      <path d="M0 -5.5 L5.5 -0.5 L4 -0.5 L4 5 L1.3 5 L1.3 1.5 L-1.3 1.5 L-1.3 5 L-4 5 L-4 -0.5 L-5.5 -0.5 Z" fill="var(--navy)"/>
    </g>

    <!-- accreditation badges -->
    <g class="accreditation-badges" fill="var(--badge)">
      <use href="#hex-badge" x="184" y="418"/>
      <use href="#hex-badge" x="256" y="418"/>
      <use href="#hex-badge" x="328" y="418"/>
      <use href="#hex-badge" x="400" y="418"/>
      <use href="#hex-badge" x="472" y="418"/>
      <use href="#hex-badge" x="544" y="418"/>
      <use href="#hex-badge" x="616" y="418"/>
    </g>
  </svg>

  <header class="holder">
    <h1 class="holder-name">ADRIAN KESTREL</h1>
    <p class="holder-role">CEO</p>
  </header>
  <p class="slogan">Transforming Lives</p>

  <ul class="contact-list">
    <li class="contact-item contact-item--phone">0412 557 093</li>
    <li class="contact-item contact-item--email">akestrel@mailbox.net</li>
    <li class="contact-item contact-item--web">www.kestrelgroup.net</li>
  </ul>

  <p class="accreditation-label">Accredited Training Provider</p>
</section>

<!-- Companies side -->
<section class="card card--companies">
  <svg class="card-art" viewBox="0 0 860 480" aria-label="Group companies: DVX, KRPE, Brivoquest, Nevo Foundation">
    <defs>
      <polygon id="hex-b" points="0,-46 42,-23 42,23 0,46 -42,23 -42,-23"/>
    </defs>

    <g class="corner-tabs" fill="var(--blue)">
      <polygon points="0,0 80,0 80,22 40,44 0,22"/>
      <polygon points="860,0 780,0 780,22 820,44 860,22"/>
      <polygon points="0,480 80,480 80,458 40,436 0,458"/>
      <polygon points="860,480 780,480 780,458 820,436 860,458"/>
    </g>

    <use href="#hex-b" x="365" y="176" fill="var(--navy)"/>
    <use href="#hex-b" x="492" y="176" fill="var(--blue)"/>
    <use href="#hex-b" x="365" y="309" fill="var(--blue)"/>
    <use href="#hex-b" x="492" y="309" fill="var(--navy)"/>

    <text class="logo-name" x="365" y="184" font-size="22">DVX</text>
    <text class="logo-name" x="492" y="183" font-size="18">KRPE</text>
    <text class="logo-name" x="365" y="314" font-size="12">Brivoquest</text>
    <text class="logo-name" x="492" y="306" font-size="13">Nevo</text>
    <text class="logo-name" x="492" y="321" font-size="11">Foundation</text>
  </svg>
</section>

</body>
</html>
```